Wordpress Design - Accounting Practice Startup

We are a relatively new Accounting Firm in Sydney with a primary focus on the Not-For-Profit sector. We need a complete re-design of our wordpress based website: www.larkmoorledgers.com.au
We already have a logo design which we would like to keep using. See uploaded files.
We have a simple menu stucture:
- Home
- About Us
- Our Services
- Contact Us
(Suggestions welcome!)
Happy for it to be a single page scrolling website linked via the menu. We would like the "Our Services" page/section to have icons for the following:
- Bookkeeping
- Payroll
- Accounting
- Training
- Consulting
- Projects
We'd like a banner at the top of the page below the menu, and a place for testimonials, possibly integrated into the body or to the side. Images and icons to be included would be great.
Our main aim is to have an elegant and modern website that works well on all devices.
Industry/Entity Type
Accounting
Colors
Designer to choose colors to be used in the design.
Look and feel
Each slider illustrates characteristics of the customer's brand and the style your logo design should communicate.

```html
<!DOCTYPE html>
<html lang="en">
<head>
<meta charset="utf-8">
<title>Larkmoor Ledgers</title>
<link rel="stylesheet" href="https://fonts.googleapis.com/css2?family=Roboto:wght@300;400;500;700&family=Open+Sans:ital,wght@0,400;0,600;1,400&display=swap">
<style>
:root{
  --green:#5cb85c;
  --green-deep:#43a047;
  --green-btn:#4caf50;
  --ink:#222;
  --body:#444;
  --muted:#666;
  --dark:#161a1d;
  --light:#f5f5f5;
  --white:#fff;
  --line:#d8d8d8;
}
*{box-sizing:border-box;margin:0;padding:0}
html,body{width:1200px;height:3051px;overflow:hidden}
body{position:relative;background:var(--white);font-family:"Open Sans",Arial,sans-serif;color:var(--body)}
.abs{position:absolute}
.center{left:0;width:1200px;text-align:center}

/* hero */
.hero{left:0;top:0;width:1200px;height:662px;z-index:2;
  clip-path:polygon(0 0,100% 0,100% 590px,50% 662px,0 590px);
  background:linear-gradient(125deg,#3c4650 0%,#6d7781 30%,#4a5661 55%,#8a949c 75%,#2f363d 100%)}
.hero-shade{left:0;top:0;width:1200px;height:662px;background:rgba(20,25,30,.45)}
.hero-edge{left:0;top:0;width:1200px;height:670px;z-index:3;pointer-events:none}
.brand{left:98px;top:28px;color:var(--white);font-family:"Roboto",sans-serif;font-weight:300;font-size:36px;line-height:38px;letter-spacing:1px;z-index:4}
.callus{right:116px;top:32px;color:var(--white);font-family:"Roboto",sans-serif;font-size:20px;z-index:4;display:flex;align-items:center;gap:8px}
.nav{right:116px;top:74px;display:flex;gap:34px;z-index:4}
.nav a{color:var(--white);text-decoration:none;font-family:"Roboto",sans-serif;font-weight:500;font-size:17px}
.hero-title{top:262px;color:var(--white);font-family:"Roboto",sans-serif;font-weight:500;font-size:52px;z-index:4}
.hero-sub{top:330px;color:var(--white);font-family:"Roboto",sans-serif;font-weight:500;font-size:15px;line-height:27px;z-index:4}
.btn{background:var(--green-btn);color:var(--white);font-family:"Roboto",sans-serif;font-weight:500;font-size:14px;border:0;border-radius:3px;display:flex;align-items:center;justify-content:center}
.hero-btn{left:541px;top:400px;width:118px;height:36px;z-index:4}
.dots{left:570px;top:607px;display:flex;gap:6px;z-index:4}
.dots span{width:14px;height:14px;border-radius:50%;border:2px solid var(--white)}
.dots span.on{background:var(--white)}

/* about */
.about{left:0;top:560px;width:1200px;height:457px;background:var(--green)}
.about-title{top:738px;color:var(--white);font-family:"Roboto",sans-serif;font-weight:500;font-size:34px}
.about-text{left:180px;width:840px;top:802px;color:var(--white);font-size:12.5px;line-height:26px;text-align:center}
.about-text p+p{margin-top:12px}

/* services */
.section-title{font-family:"Roboto",sans-serif;font-weight:500;font-size:34px;color:var(--ink)}
.services-title{top:1078px}
.service{width:320px}
.service svg{display:block;width:80px;height:80px}
.service h3{font-family:"Roboto",sans-serif;font-weight:400;font-size:21px;color:var(--ink);margin-top:20px}
.service p{font-size:12.5px;line-height:25px;color:var(--body);margin-top:6px}

/* testimonials */
.clients{left:0;top:1780px;width:1200px;height:586px;background:radial-gradient(ellipse at 50% 40%,#2b3035 0%,#161a1d 70%)}
.clients-title{top:1858px;color:var(--white);font-family:"Roboto",sans-serif;font-weight:500;font-size:34px}
.clients-sub{top:1916px;color:var(--white);font-size:14px;line-height:25px}
.quote-card{left:256px;top:2003px;width:662px;height:180px;background:var(--white);border-radius:14px}
.quote-text{left:312px;top:2026px;width:570px;font-style:italic;font-size:12.5px;line-height:25px;color:var(--body)}
.qmark{font-family:"Roboto",sans-serif;font-weight:700;font-size:34px;color:var(--ink);line-height:1}
.avatar{left:533px;top:2146px;width:102px;height:102px;border-radius:50%;border:4px solid var(--white);background:linear-gradient(160deg,#c9b8a6,#7d6f62)}
.person{top:2255px;color:var(--green);font-family:"Roboto",sans-serif;font-weight:500;font-size:14px}
.firm{top:2280px;color:var(--white);font-family:"Roboto",sans-serif;font-weight:500;font-size:15px}
.arrow{top:2060px}

/* contact */
.contact{left:0;top:2366px;width:1200px;height:543px;background:var(--light)}
.contact-title{top:2417px}
.contact-sub{top:2475px;font-size:14px;line-height:25px;color:var(--body)}
.contact-brand{left:112px;top:2570px;color:var(--ink);font-family:"Roboto",sans-serif;font-weight:300;font-size:38px;line-height:38px;letter-spacing:1px}
.info{left:108px;display:flex;gap:26px;font-size:13px;line-height:25px;color:var(--body)}
.info svg{flex:none;margin-top:4px}
.field{background:var(--white);border:1px solid var(--line);font-style:italic;font-size:12px;color:#777;padding:10px 16px;height:39px}
.send{left:441px;top:2807px;width:133px;height:34px}

/* footer */
.footer{left:0;top:2909px;width:1200px;height:142px;background:var(--green)}
.socials{left:541px;top:2943px;display:flex;gap:8px}
.socials span{width:26px;height:26px;border:2px solid var(--white);border-radius:50%}
.foot-links{top:2982px;color:var(--white);font-size:13px}
.copyright{top:3008px;color:var(--white);font-size:12px}
</style>
</head>
<body>

<!-- hero -->
<header class="abs hero" role="img" aria-label="Photo of business people reviewing financial charts and reports at a desk with a laptop">
  <div class="abs hero-shade"></div>
</header>
<svg class="abs hero-edge" viewBox="0 0 1200 670" aria-hidden="true"><polyline points="0,590 600,662 1200,590" fill="none" stroke="#fff" stroke-width="4"/></svg>

<div class="abs brand">LARKMOOR<br>LEDGERS</div>
<div class="abs callus">
  <svg width="18" height="18" viewBox="0 0 24 24"><path fill="#fff" d="M6.6 10.8a15.5 15.5 0 0 0 6.6 6.6l2.2-2.2c.3-.3.7-.4 1-.2 1.1.4 2.3.6 3.6.6.6 0 1 .4 1 1V20c0 .6-.4 1-1 1C10.6 21 3 13.4 3 4c0-.6.4-1 1-1h3.5c.6 0 1 .4 1 1 0 1.3.2 2.5.6 3.6.1.3 0 .7-.2 1z"/></svg>
  Call Us 0400 118 362
</div>
<nav class="abs nav"><a href="#home">HOME</a><a href="#about">ABOUT US</a><a href="#services">OUR SERVICES</a><a href="#contact">CONTACT US</a></nav>
<h1 class="abs center hero-title">LARKMOOR LEDGERS</h1>
<p class="abs center hero-sub">AT LARKMOOR LEDGERS, WE BELIEVE THAT EVERY NUMBER COUNTS<br>WE STRIVE TO DELIVER A PREMIUM SERVICE</p>
<a class="abs btn hero-btn">READ MORE</a>
<div class="abs dots"><span class="on"></span><span></span><span></span></div>

<!-- about -->
<section class="abs about" id="about"></section>
<h2 class="abs center about-title">ABOUT OUR COMPANY</h2>
<div class="abs about-text">
  <p>Sed ut perspiciatis unde omnis iste natus error sit voluptatem accusantium doloremque laudantium, totam rem aperiam, eaque ipsa quae ab illo inventore veritatis et quasi architecto beatae vitae dicta sunt explicabo. Nemo enim ipsam voluptatem quia voluptas sit aspernatur aut odit aut fugit, sed quia consequuntur magni dolores eos qui ratione voluptatem sequi nesciunt.</p>
  <p>Nemo enim ipsam voluptatem quia voluptas sit aspernatur aut odit aut fugit, sed quia consequuntur magni dolores eos qui ratione voluptatem sequi nesciunt. Neque porro quisquam est, qui dolorem ipsum quia dolor sit amet, consectetur</p>
</div>

<!-- services -->
<h2 class="abs center section-title services-title" id="services">OUR SERVICES</h2>

<div class="abs service" style="left:96px;top:1190px">
  <svg viewBox="0 0 80 80" fill="none" stroke="#43a047" stroke-width="2.5"><path d="M6 28 L30 16 L54 28 Z"/><path d="M12 32v28M24 32v28M36 32v28M48 32v28M4 64h52"/><circle cx="58" cy="52" r="14"/><path d="M62 46h-6a3 3 0 0 0 0 6h4a3 3 0 0 1 0 6h-6M58 43v3M58 58v3"/></svg>
  <h3>Bookkeeping</h3>
  <p>Nemo enim ipsam voluptatem quia voluptas sit aspernatur aut odit aut fugit, sed quia consequuntur magni dolores eos qui ratione voluptatem sequi nesciunt. Neque porro quisquam</p>
</div>
<div class="abs service" style="left:448px;top:1190px">
  <svg viewBox="0 0 80 80" fill="none" stroke="#43a047" stroke-width="2.5"><path d="M6 50 L40 34 L74 50 L40 66 Z"/><path d="M6 44 L40 28 L74 44"/><path d="M6 38 L40 22 L74 38"/><path d="M6 32 L40 16 L74 32"/><ellipse cx="40" cy="41" rx="8" ry="4"/></svg>
  <h3>Payroll</h3>
  <p>Nemo enim ipsam voluptatem quia voluptas sit aspernatur aut odit aut fugit, sed quia consequuntur magni dolores eos qui ratione voluptatem sequi nesciunt. Neque porro quisquam</p>
</div>
<div class="abs service" style="left:800px;top:1190px">
  <svg viewBox="0 0 80 80" fill="none" stroke="#43a047" stroke-width="2.5"><rect x="4" y="6" width="30" height="44" rx="3"/><rect x="9" y="11" width="20" height="8"/><path d="M10 26h4M18 26h4M26 26h2M10 34h4M18 34h4M26 34h2M10 42h4M18 42h4"/><path d="M30 22h28l14 14v40H30z"/><path d="M58 22v14h14"/><circle cx="51" cy="56" r="10"/><path d="M54 51h-5a2.5 2.5 0 0 0 0 5h4a2.5 2.5 0 0 1 0 5h-5"/></svg>
  <h3>Accounting</h3>
  <p>Nemo enim ipsam voluptatem quia voluptas sit aspernatur aut odit aut fugit, sed quia consequuntur magni dolores eos qui ratione voluptatem sequi nesciunt. Neque porro quisquam</p>
</div>

<div class="abs service" style="left:96px;top:1452px">
  <svg viewBox="0 0 80 80" fill="#43a047" stroke="#43a047" stroke-width="2.5"><rect x="34" y="4" width="38" height="28" fill="none"/><path d="M53 32v10" fill="none"/><circle cx="18" cy="12" r="6"/><path d="M11 22h14v20h-3v14h-8V42h-3z"/><path d="M25 26 L36 20" fill="none"/><circle cx="14" cy="58" r="5"/><circle cx="38" cy="58" r="5"/><circle cx="62" cy="58" r="5"/><path d="M6 78v-8a8 8 0 0 1 16 0v8zM30 78v-8a8 8 0 0 1 16 0v8zM54 78v-8a8 8 0 0 1 16 0v8z"/></svg>
  <h3>Training</h3>
  <p>Nemo enim ipsam voluptatem quia voluptas sit aspernatur aut odit aut fugit, sed quia consequuntur magni dolores eos qui ratione voluptatem sequi nesciunt. Neque porro quisquam</p>
</div>
<div class="abs service" style="left:448px;top:1452px">
  <svg viewBox="0 0 80 80" fill="none" stroke="#43a047" stroke-width="2.5"><path d="M40 14a18 18 0 0 0-10 33v9h20v-9a18 18 0 0 0-10-33z"/><path d="M32 62h16M34 68h12M37 74h6"/><path d="M40 2v6M14 10l4 4M66 10l-4 4M6 32h6M68 32h6"/><path d="M34 28a4 4 0 0 1 6-3 4 4 0 0 1 6 3c0 4-6 8-6 8s-6-4-6-8z"/></svg>
  <h3>Consulting</h3>
  <p>Nemo enim ipsam voluptatem quia voluptas sit aspernatur aut odit aut fugit, sed quia consequuntur magni dolores eos qui ratione voluptatem sequi nesciunt. Neque porro quisquam</p>
</div>
<div class="abs service" style="left:800px;top:1452px">
  <svg viewBox="0 0 80 80" fill="none" stroke="#43a047" stroke-width="2.5"><rect x="6" y="10" width="66" height="44"/><path d="M4 10h70M39 4v6M39 54v8M30 76l9-14 9 14"/><polyline points="14,44 28,32 38,38 56,22"/><path d="M50 22h6v6"/></svg>
  <h3>Projects</h3>
  <p>Nemo enim ipsam voluptatem quia voluptas sit aspernatur aut odit aut fugit, sed quia consequuntur magni dolores eos qui ratione voluptatem sequi nesciunt. Neque porro quisquam</p>
</div>

<!-- testimonials -->
<section class="abs clients" role="img" aria-label="Dimmed photo of an office meeting table with laptops and documents"></section>
<h2 class="abs center clients-title">WHAT OUR CLIENTS SAY</h2>
<p class="abs center clients-sub">Lorem ipsum dolor sit amet, consectetur adipiscing elit. Cras rhoncus erat ut tincidunt ultrices.<br>Sed sodales aliquam libero. Vivamus iaculis molestie orci vitae laoreet.</p>
<svg class="abs arrow" style="left:100px" width="30" height="48" viewBox="0 0 30 48"><polyline points="26,2 4,24 26,46" fill="none" stroke="#fff" stroke-width="2"/></svg>
<svg class="abs arrow" style="left:1040px" width="30" height="48" viewBox="0 0 30 48"><polyline points="4,2 26,24 4,46" fill="none" stroke="#fff" stroke-width="2"/></svg>
<div class="abs quote-card"></div>
<span class="abs qmark" style="left:278px;top:2018px">&ldquo;</span>
<p class="abs quote-text">Nemo enim ipsam voluptatem quia voluptas sit aspernatur aut odit aut fugit, sed quia constur magni dolores eos qui ratione voluptatem sequi nesciunt. Neque porro quisquam est, qui do-lorem ipsum quia dolor sit amet, consectetur, adipisci velit, sed quia non numquam eius modi tempora incidunt ut labore et dolore magnam aliquam</p>
<span class="abs qmark" style="left:672px;top:2120px">&rdquo;</span>
<div class="abs avatar" role="img" aria-label="Client portrait photo"></div>
<p class="abs center person">MAYA FENWICK</p>
<p class="abs center firm">Larkmoor Ledgers</p>

<!-- contact -->
<section class="abs contact" id="contact"></section>
<h2 class="abs center section-title contact-title">CONTACT US</h2>
<p class="abs center contact-sub">Nemo enim ipsam voluptatem quia voluptas sit aspernatur aut odit aut fugit, sed quia<br>sequatur? Quis autem vel eum iure reprehenderit qui</p>
<div class="abs contact-brand">LARKMOOR<br>LEDGERS</div>

<div class="abs info" style="top:2668px">
  <svg width="18" height="26" viewBox="0 0 18 26"><path fill="#333" d="M9 0a9 9 0 0 0-9 9c0 7 9 17 9 17s9-10 9-17a9 9 0 0 0-9-9zm0 13a4 4 0 1 1 0-8 4 4 0 0 1 0 8z"/></svg>
  <p>Larkmoor Ledgers<br>Suite 12, 48 Tallow Street,<br>Alderbrook</p>
</div>
<div class="abs info" style="top:2748px">
  <svg width="18" height="28" viewBox="0 0 18 28"><rect x="2" y="1" width="14" height="26" rx="2" fill="none" stroke="#333" stroke-width="2.5"/><path d="M2 21h14" stroke="#333" stroke-width="2"/></svg>
  <p>Phone: 0400 118 362<br>Phone: 0400 227 914</p>
</div>
<div class="abs info" style="top:2812px">
  <svg width="20" height="16" viewBox="0 0 20 16" style="margin-top:5px"><rect width="20" height="16" rx="1" fill="#333"/><polyline points="1,2 10,9 19,2" fill="none" stroke="#f5f5f5" stroke-width="1.8"/></svg>
  <p>hello@larkmoorledgers.com.au</p>
</div>

<div class="abs field" style="left:441px;top:2571px;width:314px">Your first name</div>
<div class="abs field" style="left:771px;top:2571px;width:316px">Your email</div>
<div class="abs field" style="left:441px;top:2624px;width:314px">Company Name</div>
<div class="abs field" style="left:771px;top:2624px;width:316px">Your Phone</div>
<div class="abs field" style="left:441px;top:2679px;width:646px;height:105px">Message</div>
<a class="abs btn send">SUBMIT NOW</a>

<!-- footer -->
<footer class="abs footer"></footer>
<div class="abs socials"><span></span><span></span><span></span><span></span></div>
<p class="abs center foot-links">Home &nbsp;/&nbsp; About us &nbsp;/&nbsp; Our Services &nbsp;/&nbsp; Contact us</p>
<p class="abs center copyright">©2016 - 2017 Larkmoor Ledgers, All Rights Reserved.</p>

</body>
</html>
```